Business card required for IT Consultancy Business - Tealbrook Consulting.
Company provides the whole nine yards of services across IT Architecture, design and execution.
Basically we provide consulting services to help businesses make sure their technology is enabling their business strategy.
Design for front and back required.
We would like the front of the card to inlcude:
Name
Title
Mobile number
email address
www.tbkc.com.au
Company logos attached.
Thank you
Industry/Entity Type
Business
Contact Information for Business Card
Name
Title
Mobile number
email address
www.tbkc.com.au
Look and feel
Each slider illustrates characteristics of the customer's brand and the style your logo design should communicate.

```html
<!DOCTYPE html>
<html lang="en">
<head>
<meta charset="utf-8">
<title>Tealbrook Consulting – Business Card</title>
<link rel="stylesheet" href="https://fonts.googleapis.com/css2?family=Questrial&display=swap">
<style>
  :root {
    --bg: #e9e7e4;
    --card: #1b1b1c;
    --card-edge: #1f6fb8;
    --orange: #f0612e;
    --blue: #2285d0;
    --white: #f2f2f2;
  }
  * { box-sizing: border-box; margin: 0; padding: 0; }
  html, body { width: 1200px; height: 716px; overflow: hidden; }
  body {
    background: var(--bg);
    font-family: "Questrial", "Century Gothic", sans-serif;
    display: flex;
    align-items: center;
    justify-content: center;
    gap: 50px;
  }
  .card {
    width: 525px;
    height: 300px;
    background: var(--card);
    border-radius: 4px;
    position: relative;
  }
  .card--front {
    box-shadow: 0 0 0 3px var(--card-edge);
    display: flex;
    align-items: center;
    justify-content: center;
  }
  .brand-name {
    color: var(--blue);
    font-size: 38px;
    line-height: 1.05;
    text-align: center;
    letter-spacing: 1px;
  }
  .card--back {
    display: flex;
    align-items: center;
    padding-left: 60px;
  }
  .brand-mark {
    color: var(--blue);
    font-size: 26px;
    line-height: 1.1;
    width: 150px;
  }
  .divider {
    width: 2px;
    height: 110px;
    background: var(--orange);
    margin: 0 22px 0 18px;
  }
  .person-name { color: var(--orange); font-size: 19px; }
  .person-title { color: var(--blue); font-size: 17px; margin-bottom: 12px; }
  .contact-list { list-style: none; }
  .contact-list li {
    color: var(--white);
    font-size: 18px;
    display: flex;
    align-items: center;
    gap: 8px;
    line-height: 1.35;
  }
  .contact-list svg { width: 14px; height: 14px; flex: none; }
</style>
</head>
<body>
  <section class="card card--front">
    <h1 class="brand-name">Tealbrook<br>Consulting</h1>
  </section>

  <section class="card card--back">
    <p class="brand-mark">Tealbrook Consulting</p>
    <div class="divider"></div>
    <div class="details">
      <p class="person-name">Employee Name</p>
      <p class="person-title">Title</p>
      <ul class="contact-list">
        <li>
          <svg viewBox="0 0 14 14" aria-hidden="true"><rect x="3.5" y="1" width="7" height="12" rx="1.5" fill="none" stroke="#f0612e" stroke-width="1.4"/><line x1="6" y1="11" x2="8" y2="11" stroke="#f0612e" stroke-width="1.2"/></svg>
          5050 123 456
        </li>
        <li>
          <svg viewBox="0 0 14 14" aria-hidden="true"><rect x="1" y="3" width="12" height="8.5" fill="#f0612e"/><polyline points="1,3 7,8 13,3" fill="none" stroke="#1b1b1c" stroke-width="1.2"/></svg>
          info@tbkc.com.au
        </li>
        <li>
          <svg viewBox="0 0 14 14" aria-hidden="true"><g fill="none" stroke="#f0612e" stroke-width="1.1"><circle cx="7" cy="7" r="5.8"/><ellipse cx="7" cy="7" rx="2.6" ry="5.8"/><line x1="1.2" y1="7" x2="12.8" y2="7"/></g></svg>
          www.tbkc.com.au
        </li>
      </ul>
    </div>
  </section>
</body>
</html>
```